LumoPledge Crowdfunding Website 1st Page

I am looking to have a first page created for a new crowd funding website that knocks down the biggest hurdle that creative types and start ups face, legal costs. For creative projects and innovative products, we are providing intellectual property and certain other legal services wrapped into the project costs.

I am using a white label crowdfunding platform that that has a standard look and feel of most crowdfunding sites e.g. tiles with campaigns, listing of campaigns categories, create new campaign options, and donate to campaigns etc. The white label program is branded with the LumoPledge logo and colors. At present there is a front page that is just a place holder for someone at ArtHively's great design! What I need is an eye-catching first page that visually and through content optimizes the LumoPledge brand. (There should be space for content for those looking to raise money and those looking to donate to campaigns.)

www.fundvexora.com is, of course, the reigning King of crowdfunding. They have been so successful that they no longer have to entice people to launch campaigns there. (So they don't speak as much to those looking to raise money.) Unlike Fundvexora, of the challenges is that I have two customers I need to engage. The first is the potential crowdfund campaign owner who is looking to raise money. The second customer is the donor.

I am looking for a smart page from a marketing standpoint that also grabs you. One should feel the energy of "the crowd" when they look at the page.

Some information regarding the logo: The font is Kabel BK BT. The primary blue is R33, G121, B 159. Hex21799F and the primary greenis R179, G210, B54 Hex B3D236. The third file is a slight variation on the LP logo that you are free to use as well. (Unfortunately, I don't have all the color information for that one readily available.) If you need more files, please just let me know.

Industry/Entity Type

Marketing

Font styles to use
Other font styles liked:
• Kabel Bk BT or complimentary

Requirements
Must have
• Please use the slogan "Where the crowd meets great ideas".

```html
<!DOCTYPE html>
<html lang="en">
<head>
<meta charset="utf-8">
<title>LumoPledge – Where the crowd meets great ideas</title>
<link rel="stylesheet" href="https://fonts.googleapis.com/css2?family=Open+Sans:wght@300;400;600;700&display=swap">
<style>
:root{
  --sky-top:#a7c2cd;
  --sky-mid:#7fb6c4;
  --teal:#3fbcc3;
  --teal-deep:#2fa9b0;
  --ink:#333;
  --muted:#8a8a8a;
  --soft:#a5a5a5;
  --line:#dcdcdc;
  --panel:#f4f4f4;
  --band:#e4e4e4;
  --blue:#2a86c6;
  --brand-blue:#21799f;
  --brand-green:#b3d236;
  --create:#3aa0d8;
  --red:#e8452c;
  --nav:#2f3235;
  --login:#6f9be6;
}
*{box-sizing:border-box;margin:0;padding:0}
html,body{width:684px;height:1200px;overflow:hidden}
body{
  position:relative;
  font-family:"Open Sans",Arial,sans-serif;
  color:var(--ink);
  background:linear-gradient(to bottom,var(--sky-top) 0,var(--sky-mid) 300px,var(--teal) 620px,var(--teal-deep) 1200px);
}
.crowd-backdrop{
  position:absolute;left:0;right:0;bottom:0;height:230px;
  background:linear-gradient(to bottom,rgba(40,150,158,0) 0,rgba(40,150,158,.55) 60%,rgba(35,140,148,.7) 100%);
}
.page{position:absolute;left:96px;top:0;width:492px;height:1200px;background:#fff}
.abs{position:absolute}

/* top nav */
.topnav{left:0;top:0;width:492px;height:19px;background:var(--nav)}
.topnav a{position:absolute;top:4px;font-size:8px;color:#b9bcbf;text-decoration:none}
.topnav a.current{color:#fff}
.topnav .sep{position:absolute;top:5px;width:1px;height:9px;background:#55595d}
.search{position:absolute;left:369px;top:4px;width:85px;height:12px;border-radius:2px;background:#f2f2f2;font-size:5.5px;color:#888;padding:2px 0 0 8px}
.search-btn{position:absolute;left:458px;top:4px;width:17px;height:12px;border-radius:2px;background:var(--login)}

/* header */
.header{left:0;top:19px;width:492px;height:60px;background:#fff}
.brand{position:absolute;left:21px;top:12px;display:flex;align-items:center;gap:6px}
.brand-dot{width:31px;height:31px;border-radius:50%;background:var(--brand-blue)}
.brand-name{font-size:15px;font-weight:400;color:#5a5a5a;white-space:nowrap}
.menu-item{position:absolute;top:20px}
.menu-item b{display:block;font-size:9.5px;font-weight:700;letter-spacing:.3px}
.menu-item span{display:block;font-size:7px;color:var(--soft);margin-top:1px}
.menu-discover b{color:#7cc31e}
.menu-create b{color:var(--create)}
.menu-divider{position:absolute;left:254px;top:19px;height:25px;border-left:1px dotted #bbb}
.btn-small{position:absolute;top:20px;height:15px;font-size:7px;color:#fff;text-align:center;line-height:15px;border-radius:1px}
.btn-register{left:383px;width:44px;background:linear-gradient(#86d631,#5bb31a)}
.btn-login{left:433px;width:39px;background:linear-gradient(#89aeef,#5f8fe0)}

/* hero */
.hero{left:0;top:79px;width:492px;height:198px;overflow:hidden}
.hero-art{position:absolute;inset:0;
  background:
   radial-gradient(circle at 76% 42%,#fff6b0 0,#d6ecf5 14%,rgba(120,200,90,.85) 28%,rgba(70,150,220,.6) 42%,rgba(200,200,200,0) 60%),
   linear-gradient(90deg,#b9b9b9 0,#cfcfcf 45%,#d8d8d8 100%)}
.hero h1{position:absolute;left:23px;top:37px;font-size:22px;font-weight:300;line-height:29px;color:#fff}
.hero p{position:absolute;left:23px;top:97px;width:236px;font-size:7.5px;line-height:9.5px;color:#fff}
.btn-learn{position:absolute;display:flex;align-items:center;gap:6px;height:30px;border-radius:4px;white-space:nowrap;
  background:linear-gradient(#7fd534,#3f9a0e);color:#fff;font-size:10px;padding-left:6px;box-shadow:0 2px 3px rgba(0,0,0,.25)}
.btn-learn .arrow{flex:none;width:15px;height:15px;border-radius:50%;background:#2f7d0a;display:flex;align-items:center;justify-content:center}
.hero .btn-learn{left:23px;top:144px;width:81px}

/* categories sidebar */
.categories{left:21px;top:303px;width:127px;height:203px;background:var(--panel);border:1px solid var(--line);padding:9px 9px}
.categories h2{font-size:8.3px;font-weight:600;color:#333;white-space:nowrap}
.categories .intro{font-size:5.8px;line-height:7px;color:var(--muted);margin-top:3px}
.categories ul{list-style:none;margin-top:6px}
.categories li{font-size:7.8px;font-weight:600;color:#555;height:14.5px;display:flex;align-items:center;gap:5px}
.categories li i{position:relative;width:7px;height:7px;display:inline-block}
.categories li i::before,.categories li i::after{content:"";position:absolute;background:#a9a9a9}
.categories li i::before{left:0;top:3px;width:7px;height:1.5px}
.categories li i::after{left:2.75px;top:0;width:1.5px;height:7px}
.categories li.active{color:var(--red)}
.categories li.active i::before,.categories li.active i::after{background:var(--red)}
.categories .all{display:block;margin-top:6px;font-size:6.5px;color:var(--red);font-weight:600}

/* staff picks */
.picks-title{left:174px;top:299px;font-size:15px;font-weight:600;color:#333}
.picks-title span{color:var(--red)}
.picks-more{left:379px;top:313px;font-size:6.5px;color:#666}
.picks-more b{color:var(--red);font-weight:400}
.feature{left:174px;top:327px;width:283px;height:177px;border:3px solid var(--line);background:#fff}
.feature-img{position:absolute;left:6px;top:7px;width:133px;height:102px;border:1px solid #ccc;
  background:linear-gradient(135deg,#3a5a9c 0,#c8443a 35%,#5c7f3c 60%,#d9a23a 80%,#3b3b6e 100%)}
.feature h3{position:absolute;left:146px;top:5px;width:132px;font-size:11.5px;line-height:14px;font-weight:700;color:var(--blue)}
.feature .byline{position:absolute;left:146px;top:38px;font-size:5.8px;color:var(--muted)}
.feature .byline b{color:#6aa820;font-weight:600}
.feature .desc{position:absolute;left:146px;top:50px;width:127px;font-size:6.2px;line-height:8.2px;color:var(--muted)}
.feature-stats{position:absolute;left:0;bottom:0;width:277px;height:52px;background:#efefef;border-top:1px solid var(--line)}
.funded-ring{position:absolute;left:10px;top:7px;width:38px;height:38px;border-radius:50%;border:3px solid #7cd34a;background:#fff;text-align:center}
.funded-ring b{display:block;font-size:8.5px;color:#5fb21d;margin-top:8px;line-height:9px}
.funded-ring small{display:block;font-size:3.8px;color:#5fb21d}
.stat{position:absolute;top:10px;text-align:center}
.stat small{display:block;font-size:6px;color:var(--muted);letter-spacing:.2px}
.stat b{display:block;font-size:13px;font-weight:400;color:#333;margin-top:1px}
.stat-div{position:absolute;top:8px;width:1px;height:36px;background:#d8d8d8}

/* popular */
.popular{left:0;top:525px;width:492px;height:241px;background:var(--band)}
.popular h2{position:absolute;left:19px;top:4px;font-size:15px;font-weight:600;color:#333}
.card{position:absolute;top:37px;width:104px;height:188px;background:#fff;border:2px solid #d4d4d4}
.card-img{height:72px;background:linear-gradient(160deg,#3d3d3d,#707070 55%,#2b2b2b)}
.card-img.photo{background:linear-gradient(160deg,#555,#9a9a9a 45%,#3a3a3a)}
.card h4{font-size:7.5px;font-weight:400;color:var(--blue);margin:3px 0 0 4px}
.card .by{font-size:5px;color:var(--muted);margin-left:4px}
.card .blurb{font-size:5.6px;line-height:7.2px;color:var(--muted);margin:4px 4px 0}
.card .loc{position:absolute;left:4px;top:128px;font-size:5.3px;color:var(--muted);display:flex;align-items:center;gap:3px}
.card .rule{position:absolute;left:0;right:0;top:138px;border-top:1px solid #e6e6e6}
.card .raised{position:absolute;left:4px;top:142px;color:var(--blue)}
.card .raised b{display:block;font-size:10px;line-height:10px}
.card .raised small{display:block;font-size:4.6px;color:#444;font-weight:700;margin-bottom:2px}
.card .ring{position:absolute;right:4px;top:142px}

/* discover mosaic */
.mosaic{left:17px;top:788px;width:458px;height:171px;display:grid;grid-template-columns:repeat(8,1fr);grid-template-rows:repeat(4,1fr);gap:1px;background:#fff}
.tile{background:#8fb5d6}
.t-plane{background:linear-gradient(135deg,#b33a2e,#8aa0b8)}
.t-sky{background:linear-gradient(180deg,#7fa9d8,#c9b29a)}
.t-shoe{background:linear-gradient(135deg,#8a8a80,#3d8fc4)}
.t-rock{background:linear-gradient(135deg,#9a9a9a,#6b6b6b)}
.discover-box{left:74px;top:830px;width:343px;height:86px;background:#fff}
.discover-box h2{position:absolute;left:14px;top:6px;font-size:15px;font-weight:400;color:#444;white-space:nowrap}
.discover-box h2 b{color:var(--blue);font-weight:700}
.discover-box p{position:absolute;left:15px;top:36px;width:200px;font-size:8.8px;line-height:11px;color:#666}
.discover-box .btn-learn{left:222px;top:35px;width:84px}

/* promo band */
.promo{left:-12px;top:984px;width:516px;height:58px;background:#e9e9e9;box-shadow:0 2px 4px rgba(0,0,0,.15)}
.promo h2{position:absolute;left:35px;top:8px;font-size:11.3px;font-weight:700;color:#333;white-space:nowrap}
.promo p{position:absolute;left:35px;top:23px;width:305px;font-size:8.3px;line-height:9.5px;color:#777}
.btn-plain{position:absolute;left:387px;top:28px;width:68px;height:22px;background:linear-gradient(#7fd534,#3f9a0e);color:#fff;font-size:9px;text-align:center;line-height:22px;border-radius:2px;white-space:nowrap}

/* footer */
.footer-col{top:1059px;width:110px}
.footer-col h5{font-size:6.5px;font-weight:700;color:#333;margin-bottom:6px}
.footer-col p{font-size:5.8px;line-height:9px;color:var(--muted)}
.footer-col .tweet b{color:var(--red);font-weight:400}
.footer-col .ago{font-style:italic;color:#b0b0b0}
.email-field{margin-top:6px;width:106px;height:16px;border:1px solid #ccc;font-size:5.6px;color:#999;padding:4px 0 0 4px}
.btn-signup{margin-top:5px;width:44px;height:16px;background:linear-gradient(#7fd534,#3f9a0e);color:#fff;font-size:6.5px;font-weight:700;text-align:center;line-height:16px}
.links{display:grid;grid-template-columns:58px 58px}
.links span{font-size:5.8px;line-height:11.5px;color:var(--muted)}
.links span.hot{color:var(--red)}

.bottombar{left:0;top:1169px;width:492px;height:31px;border-top:1px solid #e4e4e4}
.bottombar .brand{left:21px;top:7px;gap:5px}
.bottombar .brand-dot{width:17px;height:17px;background:#cfcfcf}
.bottombar .brand-name{font-size:10px;color:#b5b5b5}
.copyright{position:absolute;right:12px;top:12px;font-size:6.3px;color:#aaa}
.copyright b{color:var(--blue);font-weight:400}
</style>
</head>
<body>
<div class="crowd-backdrop" role="img" aria-label="Faint silhouettes of a cheering crowd"></div>

<div class="page">
  <nav class="topnav abs">
    <a class="current" style="left:22px">Home</a>
    <span class="sep" style="left:58px"></span>
    <a style="left:72px">About</a>
    <span class="sep" style="left:104px"></span>
    <a style="left:117px">Help</a>
    <span class="sep" style="left:144px"></span>
    <a style="left:156px">Contact</a>
    <div class="search">Search Projects</div>
    <div class="search-btn"></div>
  </nav>

  <header class="header abs">
    <div class="brand"><span class="brand-dot"></span><span class="brand-name">LumoPledge</span></div>
    <div class="menu-item menu-discover" style="left:192px"><b>DISCOVER</b><span>Great Projects</span></div>
    <div class="menu-divider"></div>
    <div class="menu-item menu-create" style="left:268px"><b>CREATE</b><span>Your Project</span></div>
    <div class="btn-small btn-register">Register</div>
    <div class="btn-small btn-login">Login</div>
  </header>

  <section class="hero abs">
    <div class="hero-art" role="img" aria-label="Grey mosaic backdrop with a glowing light bulb in colourful tiles"></div>
    <h1>Need Funds for your<br>Creative Ideas ?</h1>
    <p>Legal costs stop too many great ideas. We wrap intellectual property protection and other key legal services into your project costs, so creators and start-ups can launch with confidence.</p>
    <div class="btn-learn"><span class="arrow"><svg width="6" height="7" viewBox="0 0 6 7"><path d="M0 0L6 3.5 0 7z" fill="#fff"/></svg></span>Learn More</div>
  </section>

  <aside class="categories abs">
    <h2>Welcome to LumoPledge</h2>
    <p class="intro">Browse projects by category and back the ideas you love most.</p>
    <ul>
      <li><i></i>Design</li>
      <li><i></i>Fashion</li>
      <li><i></i>Film</li>
      <li><i></i>Games</li>
      <li class="active"><i></i>Comics</li>
      <li><i></i>Design</li>
      <li><i></i>Fashion</li>
      <li><i></i>Film</li>
      <li><i></i>Games</li>
    </ul>
    <span class="all">+ View all categories</span>
  </aside>

  <h2 class="picks-title abs">Staff Picks : <span>Comics</span></h2>
  <div class="picks-more abs">See all <b>18</b> Comic Projects</div>

  <article class="feature abs">
    <div class="feature-img" role="img" aria-label="Comic book cover artwork with a team of costumed heroes"></div>
    <h3>Starforge Comics Series Special Edition</h3>
    <div class="byline">by <b>Rowan Pell</b> in <svg width="4" height="6" viewBox="0 0 4 6"><path d="M2 0a2 2 0 0 1 2 2C4 3.5 2 6 2 6S0 3.5 0 2a2 2 0 0 1 2-2z" fill="#6aa820"/></svg> London, UK</div>
    <p class="desc">Lorem ipsum dolor sit amet, consectetur adipiscing elit. Donec mattis consequat massa, a rhoncus nunc facilisis vel. Maecenas tristique orci dui. Donec mattis consequat massa, a rhoncus nunc facilisis vel. Maecenas tristique orci dui.</p>
    <div class="feature-stats">
      <div class="funded-ring"><b>156%</b><small>FUNDED</small></div>
      <div class="stat" style="left:74px;width:54px"><small>BACKERS</small><b>240</b></div>
      <div class="stat-div" style="left:133px"></div>
      <div class="stat" style="left:135px;width:60px"><small>PLEDGED</small><b>£15,600</b></div>
      <div class="stat-div" style="left:198px"></div>
      <div class="stat" style="left:200px;width:55px"><small>DAYS LEFT</small><b>04</b></div>
    </div>
  </article>

  <section class="popular abs">
    <h2>Popular</h2>

    <article class="card" style="left:19px">
      <div class="card-img" role="img" aria-label="Chalkboard menu with hand lettering"></div>
      <h4>CAFE BENVOLO</h4>
      <div class="by">by Cafe Benvolo</div>
      <p class="blurb">Help Cafe Benvolo nourish our local community by supporting our Vegetarian Bakery Cafe.</p>
      <div class="loc"><svg width="4" height="6" viewBox="0 0 4 6"><path d="M2 0a2 2 0 0 1 2 2C4 3.5 2 6 2 6S0 3.5 0 2a2 2 0 0 1 2-2z" fill="#2a86c6"/></svg>London, UK</div>
      <div class="rule"></div>
      <div class="raised"><b>£2000</b><small>RAISED</small><b>18</b><small>DAYS LEFT</small></div>
      <svg class="ring" width="40" height="40" viewBox="0 0 40 40"><circle cx="20" cy="20" r="17" fill="#fff" stroke="#e6e6e6" stroke-width="3"/><circle cx="20" cy="20" r="17" fill="none" stroke="#7cd34a" stroke-width="3" pathLength="100" stroke-dasharray="25 100" transform="rotate(-90 20 20)"/><text x="20" y="21" text-anchor="middle" font-size="8.5" font-weight="700" fill="#2a86c6" font-family="Open Sans,sans-serif">25%</text><text x="20" y="27" text-anchor="middle" font-size="3.6" font-weight="700" fill="#2a86c6" font-family="Open Sans,sans-serif">FUNDED</text></svg>
    </article>

    <article class="card" style="left:136px">
      <div class="card-img photo" role="img" aria-label="Black and white portrait photograph"></div>
      <h4>PORTRAITS IV</h4>
      <div class="by">by Lena Moretti</div>
      <p class="blurb">Bring portrait photography into your living room and support local charities through my studio project.</p>
      <div class="loc"><svg width="4" height="6" viewBox="0 0 4 6"><path d="M2 0a2 2 0 0 1 2 2C4 3.5 2 6 2 6S0 3.5 0 2a2 2 0 0 1 2-2z" fill="#2a86c6"/></svg>Surrey, UK</div>
      <div class="rule"></div>
      <div class="raised"><b>£3456</b><small>RAISED</small><b>23</b><small>DAYS LEFT</small></div>
      <svg class="ring" width="40" height="40" viewBox="0 0 40 40"><circle cx="20" cy="20" r="17" fill="#fff" stroke="#e6e6e6" stroke-width="3"/><circle cx="20" cy="20" r="17" fill="none" stroke="#7cd34a" stroke-width="3" pathLength="100" stroke-dasharray="33 100" transform="rotate(-90 20 20)"/><text x="20" y="21" text-anchor="middle" font-size="8.5" font-weight="700" fill="#2a86c6" font-family="Open Sans,sans-serif">33%</text><text x="20" y="27" text-anchor="middle" font-size="3.6" font-weight="700" fill="#2a86c6" font-family="Open Sans,sans-serif">FUNDED</text></svg>
    </article>

    <article class="card" style="left:254px">
      <div class="card-img" role="img" aria-label="Chalkboard menu with hand lettering"></div>
      <h4>CAFE BENVOLO</h4>
      <div class="by">by Cafe Benvolo</div>
      <p class="blurb">Help Cafe Benvolo nourish our local community by supporting our Vegetarian Bakery Cafe.</p>
      <div class="loc"><svg width="4" height="6" viewBox="0 0 4 6"><path d="M2 0a2 2 0 0 1 2 2C4 3.5 2 6 2 6S0 3.5 0 2a2 2 0 0 1 2-2z" fill="#2a86c6"/></svg>London, UK</div>
      <div class="rule"></div>
      <div class="raised"><b>£2000</b><small>RAISED</small><b>18</b><small>DAYS LEFT</small></div>
      <svg class="ring" width="40" height="40" viewBox="0 0 40 40"><circle cx="20" cy="20" r="17" fill="#fff" stroke="#e6e6e6" stroke-width="3"/><circle cx="20" cy="20" r="17" fill="none" stroke="#7cd34a" stroke-width="3" pathLength="100" stroke-dasharray="25 100" transform="rotate(-90 20 20)"/><text x="20" y="21" text-anchor="middle" font-size="8.5" font-weight="700" fill="#2a86c6" font-family="Open Sans,sans-serif">25%</text><text x="20" y="27" text-anchor="middle" font-size="3.6" font-weight="700" fill="#2a86c6" font-family="Open Sans,sans-serif">FUNDED</text></svg>
    </article>

    <article class="card" style="left:372px">
      <div class="card-img photo" role="img" aria-label="Black and white portrait photograph"></div>
      <h4>PORTRAITS IV</h4>
      <div class="by">by Lena Moretti</div>
      <p class="blurb">Bring portrait photography into your living room and support local charities through my studio project.</p>
      <div class="loc"><svg width="4" height="6" viewBox="0 0 4 6"><path d="M2 0a2 2 0 0 1 2 2C4 3.5 2 6 2 6S0 3.5 0 2a2 2 0 0 1 2-2z" fill="#2a86c6"/></svg>Surrey, UK</div>
      <div class="rule"></div>
      <div class="raised"><b>£3456</b><small>RAISED</small><b>23</b><small>DAYS LEFT</small></div>
      <svg class="ring" width="40" height="40" viewBox="0 0 40 40"><circle cx="20" cy="20" r="17" fill="#fff" stroke="#e6e6e6" stroke-width="3"/><circle cx="20" cy="20" r="17" fill="none" stroke="#7cd34a" stroke-width="3" pathLength="100" stroke-dasharray="33 100" transform="rotate(-90 20 20)"/><text x="20" y="21" text-anchor="middle" font-size="8.5" font-weight="700" fill="#2a86c6" font-family="Open Sans,sans-serif">33%</text><text x="20" y="27" text-anchor="middle" font-size="3.6" font-weight="700" fill="#2a86c6" font-family="Open Sans,sans-serif">FUNDED</text></svg>
    </article>
  </section>

  <div class="mosaic abs" role="img" aria-label="Grid of project photos: paper plane, mountain sky, sneakers and rocks">
    <div class="tile t-plane"></div><div class="tile t-sky"></div><div class="tile t-shoe"></div><div class="tile t-plane"></div><div class="tile t-sky"></div><div class="tile t-sky"></div><div class="tile t-rock"></div><div class="tile t-shoe"></div>
    <div class="tile t-plane"></div><div class="tile"></div><div class="tile"></div><div class="tile"></div><div class="tile"></div><div class="tile"></div><div class="tile"></div><div class="tile t-plane"></div>
    <div class="tile t-shoe"></div><div class="tile"></div><div class="tile"></div><div class="tile"></div><div class="tile"></div><div class="tile"></div><div class="tile"></div><div class="tile t-shoe"></div>
    <div class="tile t-sky"></div><div class="tile t-sky"></div><div class="tile t-rock"></div><div class="tile t-plane"></div><div class="tile t-sky"></div><div class="tile t-sky"></div><div class="tile t-rock"></div><div class="tile t-plane"></div>
  </div>
  <div class="discover-box abs">
    <h2><b>Discover</b> great projects and Support them!</h2>
    <p>Back the creators you believe in and watch their ideas come to life, one pledge at a time.</p>
    <div class="btn-learn"><span class="arrow"><svg width="6" height="7" viewBox="0 0 6 7"><path d="M0 0L6 3.5 0 7z" fill="#fff"/></svg></span>Learn More</div>
  </div>

  <section class="promo abs">
    <h2>Where the crowd meets great ideas – with legal protection built into every project</h2>
    <p>Raising money? Patent, trademark and copyright help come wrapped into your campaign costs. Giving? Your pledge backs ideas that are protected and ready to grow.</p>
    <div class="btn-plain">Learn More</div>
  </section>

  <div class="footer-col abs" style="left:21px">
    <h5>ABOUT</h5>
    <p>Donec rutrum elit ac arcu bibendum rhoncus in vitae turpis. Quisque fermentum gravida eros non faucibus. Curabitur fermentum, arcu sed cursus commodo.</p>
    <p style="margin-top:7px">sales@brightwebworks.com<br>+1 (555) 010 - 20 - 30</p>
  </div>
  <div class="footer-col abs" style="left:136px">
    <h5>RECENT TWEETS</h5>
    <p class="tweet"><b>@brightweb</b> &nbsp;Vivamus porta dui dapibus erat egestas semper. In quis sem neque<br><span class="ago">5 minutes ago</span></p>
    <p class="tweet" style="margin-top:5px"><b>@brightweb</b> &nbsp;Vivamus porta dui dapibus erat egestas semper. In quis sem neque<br><span class="ago">1 day ago</span></p>
  </div>
  <div class="footer-col abs" style="left:252px">
    <h5>NEWSLETTER SIGNUP</h5>
    <p>Donec rutrum elit ac arcu bibendum rhoncus in vitae turpis.</p>
    <div class="email-field">Enter your e-mail address</div>
    <div class="btn-signup">SIGNUP</div>
  </div>
  <div class="footer-col abs" style="left:367px">
    <h5>DISCOVER &amp; CREATE</h5>
    <div class="links">
      <span>What</span><span>Staff Picks</span>
      <span>Start a project</span><span>Popular</span>
      <span>Project Guidlines</span><span class="hot">Recent</span>
      <span>Press</span><span>Small Projects</span>
      <span>Stats</span><span>Most Funded</span>
    </div>
  </div>

  <footer class="bottombar abs">
    <div class="brand abs"><span class="brand-dot"></span><span class="brand-name">LumoPledge</span></div>
    <div class="copyright">2013 Copyright <b>LumoPledge</b> | All rights reserved.</div>
  </footer>
</div>
</body>
</html>
```